Management Consulting needing a cool business card for client acquisition and networking

We are looking for a business card that is progressive and fresh that conveys innovation, forward thinking, and confidence. The business card is for a company based in Charlotte NC called, 'VELMORE CONSULTING GROUP LLC'. The company primarily works with banks, insurance, and brokerages to implement innovative solutions to help them streamline their operations, to more effectively manage risks, and to improve their customer relationships.

Target Market(s)

Typically meet with Chief Financial Officers, Chief Information Officers, Chief Operations Officer, Business Unit Leader. The target market are generally 40-55 years, male, white, master level education plus.

Industry/Entity Type

Progressive

Font styles to use
Serif
Other font styles liked:
• Calibri

Requirements
Should not have
• Designs that look too much like law firms or accounting companies. Too conservative

```html
<!DOCTYPE html>
<html lang="en">
<head>
<meta charset="utf-8">
<title>Velmore Consulting Group LLC – Business Card</title>
<link href="https://fonts.googleapis.com/css2?family=Cabin:wght@400;700&display=swap" rel="stylesheet">
<style>
  :root{
    --navy:#1f2559;
    --navy-deep:#171c47;
    --navy-light:#2c3472;
    --red:#c8102e;
    --white:#ffffff;
    --paper:#f4f4f6;
    --silver:#d4d6e2;
    --stage:#2a2a2c;
  }
  *{margin:0;padding:0;box-sizing:border-box}
  html,body{width:1200px;height:900px;overflow:hidden}
  body{
    background:var(--stage);
    font-family:"Cabin",sans-serif;
    display:flex;flex-direction:column;align-items:center;justify-content:center;gap:56px;
  }
  .card{
    width:640px;height:366px;border-radius:22px;position:relative;overflow:hidden;
    box-shadow:0 12px 30px rgba(0,0,0,.45);
  }
  /* Front */
  .card-front{
    background:radial-gradient(ellipse at 40% 35%,var(--navy-light) 0%,var(--navy) 55%,var(--navy-deep) 100%);
    display:flex;align-items:center;justify-content:center;
  }
  .front-name{
    color:var(--silver);font-size:28px;font-weight:400;letter-spacing:1.5px;
  }
  /* Back */
  .card-back{background:linear-gradient(180deg,var(--white) 0%,var(--paper) 100%)}
  .back-company{
    position:absolute;top:40px;right:36px;
    color:var(--navy);font-size:22px;font-weight:400;letter-spacing:1px;
  }
  .back-rule{position:absolute;top:86px;left:260px;right:0;height:2px;background:var(--red)}
  .person{position:absolute;top:104px;left:40px}
  .person-name{color:var(--red);font-size:22px;font-weight:400;letter-spacing:.5px}
  .person-title{color:var(--navy);font-size:16px;font-weight:700;margin-top:2px}
  .person-rule{width:250px;height:2px;background:var(--red);margin-top:10px}
  .contact-list{position:absolute;top:186px;left:40px;list-style:none}
  .contact-list li{
    display:flex;align-items:center;gap:10px;
    color:var(--navy);font-size:16px;line-height:26px;
  }
  .contact-list svg{width:15px;height:15px;flex:none}
  .address-band{
    position:absolute;left:0;right:0;bottom:0;height:62px;background:var(--navy);
    color:var(--white);font-size:17px;
    display:flex;align-items:center;justify-content:flex-end;padding-right:40px;
  }
</style>
</head>
<body>

<section class="card card-front" aria-label="Card front">
  <div class="front-name">Velmore Consulting Group LLC</div>
</section>

<section class="card card-back" aria-label="Card back">
  <div class="back-company">Velmore Consulting Group LLC</div>
  <div class="back-rule"></div>

  <div class="person">
    <div class="person-name">MARCUS J. TALLIS</div>
    <div class="person-title">chief solutions architect</div>
    <div class="person-rule"></div>
  </div>

  <ul class="contact-list">
    <li>
      <svg viewBox="0 0 16 16"><path fill="var(--red)" d="M4 1.5l2.3 3-1.4 1.6c.8 2 2.3 3.5 4.4 4.4l1.6-1.4 3 2.3-1.6 2.6C7.2 14 2 8.8 1.5 3.1z"/></svg>
      <span>704 555 0182</span>
    </li>
    <li>
      <svg viewBox="0 0 16 16"><rect x="4" y="1" width="8" height="14" rx="1.5" fill="none" stroke="var(--red)" stroke-width="1.8"/><circle cx="8" cy="12.3" r="1" fill="var(--red)"/></svg>
      <span>704 555 0147</span>
    </li>
    <li>
      <svg viewBox="0 0 16 16"><rect x="1" y="3" width="14" height="10" fill="var(--red)"/><path d="M1.5 3.5L8 9l6.5-5.5" fill="none" stroke="var(--white)" stroke-width="1.2"/></svg>
      <span>mtallis@velmoreconsulting.com</span>
    </li>
    <li>
      <svg viewBox="0 0 16 16"><circle cx="8" cy="8" r="6.5" fill="var(--red)"/><g fill="none" stroke="var(--white)" stroke-width="1"><ellipse cx="8" cy="8" rx="2.8" ry="6.5"/><path d="M1.5 8h13M2.5 5h11M2.5 11h11"/></g></svg>
      <span>www.velmoreconsulting.com</span>
    </li>
  </ul>

  <div class="address-band">1820 Linden Park rd., Suite 300, Charlotte, NC 28209</div>
</section>

</body>
</html>
```